11 x 11 Flyer Design for Social Media - Reverse Mortgages

62 or older?

A Reverse Mortgage
could be
Your Road to Financial Freedom

* No Monthly Payments
* No Income Requirements
* No Credit Score Requirements
* No Loss of Ownership

Receive cash by lump sum, monthly installments or a line of credit!!

Call us today for a Free Consultation!!
(800) 471-2965

Bluegate Financial Services, Inc.
NMLS #318760
www.bluegatehome.com

```html
<!DOCTYPE html>
<html lang="en">
<head>
<meta charset="utf-8">
<title>Reverse Mortgage Flyer – Bluegate Financial Services</title>
<link href="https://fonts.googleapis.com/css2?family=Jost:wght@400;500;700;800&display=swap" rel="stylesheet">
<style>
  :root {
    --blue-light: #2299d8;
    --blue-mid: #1c8fd2;
    --blue-deep: #0a67b3;
    --blue-edge: #0b4e8e;
    --white: #ffffff;
    --ink: #222222;
    --brand-blue: #1f63ad;
  }
  * { margin: 0; padding: 0; box-sizing: border-box; }
  html, body { width: 1200px; height: 1200px; overflow: hidden; background: var(--white); }
  .flyer {
    position: relative;
    width: 1200px; height: 1200px;
    overflow: hidden;
    font-family: "Jost", "Futura", sans-serif;
    color: var(--white);
    background: linear-gradient(90deg, var(--blue-light) 0%, var(--blue-mid) 55%, var(--blue-deep) 100%);
  }
  .footer-band {
    position: absolute; left: 0; top: 1121px; width: 1200px; height: 79px;
    background: var(--white);
  }
  .photo-strip { position: absolute; left: 0; top: 0; width: 1200px; height: 1200px; }
  .brand-box {
    position: absolute; left: 197px; top: 55px; width: 429px; height: 252px;
    background: var(--white);
    display: flex; align-items: center; justify-content: center; gap: 14px;
  }
  .brand-mark { width: 26px; height: 26px; border-radius: 50%; background: var(--brand-blue); }
  .brand-name { font-size: 25px; font-weight: 500; color: var(--brand-blue); text-align: left; line-height: 1.2; }
  .headline {
    position: absolute; left: 52px; top: 334px;
    font-size: 103px; font-weight: 800; letter-spacing: 0; line-height: 1;
  }
  .subhead {
    position: absolute; left: 54px; top: 434px;
    font-size: 22px; font-weight: 400; letter-spacing: 0.2px;
  }
  .benefits { position: absolute; left: 92px; top: 479px; list-style: none; }
  .benefits li {
    display: flex; align-items: center; height: 81px;
    font-size: 46px; font-weight: 500; letter-spacing: 0.3px;
  }
  .benefits svg { width: 32px; height: 32px; margin-right: 25px; flex: none; }
  .payout {
    position: absolute; left: 52px; top: 827px;
    font-size: 22px; font-weight: 400;
  }
  .cta {
    position: absolute; left: 52px; top: 905px;
    font-size: 36px; font-weight: 800; letter-spacing: 0.6px;
  }
  .phone {
    position: absolute; left: 52px; top: 960px;
    display: flex; align-items: center;
    font-size: 76px; font-weight: 700; letter-spacing: 1px; line-height: 1;
  }
  .phone svg { width: 30px; height: 42px; margin-right: 18px; }
  .company {
    position: absolute; left: 56px; top: 1052px;
    font-size: 23px; font-weight: 400; line-height: 1.25;
  }
  .website {
    position: absolute; left: 215px; top: 1140px;
    font-size: 30px; font-weight: 400; color: var(--ink); letter-spacing: 0.5px;
  }
</style>
</head>
<body>
<div class="flyer">
  <div class="footer-band"></div>

  <svg class="photo-strip" viewBox="0 0 1200 1200">
    <defs>
      <linearGradient id="warm" x1="0" y1="0" x2="1" y2="1">
        <stop offset="0" stop-color="#e3d2c0"/><stop offset="1" stop-color="#8a6650"/>
      </linearGradient>
      <linearGradient id="sky" x1="0" y1="0" x2="1" y2="1">
        <stop offset="0" stop-color="#dfe8ee"/><stop offset="1" stop-color="#9a7b64"/>
      </linearGradient>
    </defs>
    <g fill="var(--blue-edge)">
      <polygon points="990,81 1065,6 1200,6 1200,262 1182,262"/>
      <polygon points="794,273 974,99 1151,279 971,456"/>
      <polygon points="890,571 1108,354 1325,571 1108,789"/>
      <polygon points="1036,903 1196,744 1200,744 1200,1062"/>
      <polygon points="841,1105 971,925 1200,1149 1200,1200 1005,1200"/>
    </g>
    <polygon role="img" aria-label="Photo: senior woman looking at her phone" fill="url(#warm)" points="994,75 1069,0 1200,0 1200,256 1186,256"/>
    <polygon role="img" aria-label="Photo: smiling senior couple in a convertible" fill="url(#sky)" points="798,267 978,93 1155,273 975,450"/>
    <polygon role="img" aria-label="Photo: laughing senior couple in white outdoors" fill="url(#sky)" points="894,565 1112,348 1329,565 1112,783"/>
    <polygon role="img" aria-label="Photo: close-up of a senior couple" fill="url(#warm)" points="1040,897 1200,738 1200,1056"/>
    <polygon role="img" aria-label="Photo: senior couple laughing together" fill="url(#warm)" points="845,1099 975,919 1200,1143 1200,1200 1000,1200"/>
  </svg>

  <div class="brand-box">
    <span class="brand-mark"></span>
    <span class="brand-name">Bluegate<br>Financial Services, Inc.</span>
  </div>

  <h1 class="headline">62 OR OLDER?</h1>
  <p class="subhead">A REVERSE MORTGAGE COULD BE YOUR ROAD TO FINANCIAL FREEDOM</p>

  <ul class="benefits">
    <li><svg viewBox="0 0 32 32"><rect x="2" y="8" width="22" height="22" fill="none" stroke="#fff" stroke-width="3"/><path d="M7 18 l6 6 L29 4" fill="none" stroke="#fff" stroke-width="4"/></svg>NO MONTHLY PAYMENTS</li>
    <li><svg viewBox="0 0 32 32"><rect x="2" y="8" width="22" height="22" fill="none" stroke="#fff" stroke-width="3"/><path d="M7 18 l6 6 L29 4" fill="none" stroke="#fff" stroke-width="4"/></svg>NO INCOME REQUIREMENTS</li>
    <li><svg viewBox="0 0 32 32"><rect x="2" y="8" width="22" height="22" fill="none" stroke="#fff" stroke-width="3"/><path d="M7 18 l6 6 L29 4" fill="none" stroke="#fff" stroke-width="4"/></svg>NO CREDIT SCORE REQUIREMENTS</li>
    <li><svg viewBox="0 0 32 32"><rect x="2" y="8" width="22" height="22" fill="none" stroke="#fff" stroke-width="3"/><path d="M7 18 l6 6 L29 4" fill="none" stroke="#fff" stroke-width="4"/></svg>NO LOSS OF OWNERSHIP</li>
  </ul>

  <p class="payout">RECEIVE CASH BY LUMP SUM, MONTHLY INSTALLMENTS OR A LINE OF CREDIT!!</p>
  <p class="cta">CALL US TODAY FOR A FREE CONSULTATION!!</p>
  <p class="phone"><svg viewBox="0 0 30 42"><path d="M10 2 C3 6 1 14 3 24 C6 34 13 40 20 40 L26 34 L19 27 L15 30 C11 27 9 20 10 14 L15 12 L14 2 Z" fill="#fff"/></svg>800.471.2965</p>
  <p class="company">BLUEGATE FINANCIAL SERVICES, INC.<br>NMLS #318760</p>
  <p class="website">WWW.BLUEGATEHOME.COM</p>
</div>
</body>
</html>
```